COMPANY NAME: Brightmoor Paths: Task Description: We are a new UK based business with global rea

Target Market

- Personal and professional development – 30-55 age group, corporate leaders, Eastern European and Asian markets
- On-assignment projects – Corporate market – Eastern European and Asian Markets
- Property investment - 35-65 age group, Europe, USA, Australia

What we need

We need logos and brand design for a suite of web platforms (website, twitter and Facebook profile). We would like to have a cohesive and consistent look across all of our online platforms. The design suite must therefore include social media logos, backgrounds and headers. Specifically we are looking for:

a. Facebook header/page design: likely to have a more youthful look

b. Website: Header, background and layout that is responsive to devices, iPhone primarily, then tablet, then PC (we have purchased a website building package from GoDaddy so if you are familiar with one of their themes, it would be great to have a design that fits with a theme you would recommend); Design should be able to accommodate a place to position video in the medium term but an image in the short term.

c. LinkedIn: header/logo; more corporate look

d. Twitter: background/logo

e. Powerpoint template: background and logo - simple and soft background not busy

f. Electronic Newsletter: logo, header and sidebar; simple and soft background not busy

h. Business card: sophisticated and simple

Colors

We have in mind a preference for colors from the purple family, maybe lavender, so as to appeal to all genders and age groups. Though we are happy to go with a recommendation if you think otherwise.

We would like a look that is professional, airy, bright, fresh, futuristic, insightful, friendly.

Ethos of the brand

- experiencing opportunity and being fulfilled in a changing world
- services are facilitated through insights
- support provided through our product, services and tailored approach to coaching/partnerships (which includes private client match-making)
- we are service providers and passionate about quality and modern leadership skills at all stages in life.

The company name is "Brightmoor Paths” - our main message is helping people move to the next level - through investments, personal and professional growth.

Some of our messaging

1. International Leadership in a new world.

2. New technology;

3. Informed;

4. Positively Influential

5. Making a difference;

6. Empowered;

7. Risk free investments;

8. Commercial opportunity;

9. Fulfilled living;

10. Carefree and Fun Living;

11. Progression;

12. Open-minded

13. Energy/dynamic

The Business:
The business is to move people very quickly out of situations that hold them back. the situations could be their own personal situations; their career; their jobs; their teams; their ideas; their finances; their financial opportunities. Remove their fears and give them the strategies to take action. The team are international and have 40 years experience between them in this area.

We do want to come across modern and dynamic, customer outcome focussed, building long-term relationships; international.
Updates

Project Deadline Extended
Reason: We have not found the right designs - we are not just looking for a website design but also images and logos. Most images we can see in the designs are stock images - very standard. We need an image which will be the face of the company, like the shop front window. This main image will be used on social media (top image) and also the home page of the website.

Target Market(s)

30-55 years
Eastern Europe; UK; Asia; Africa; Middle East
Personal, Professional, Corporate, and Financial Growth

Industry/Entity Type

Business Service

Contact Information for Business Card

Simple and stylish
the 3 areas of the business on the reverse -

International look - Offices in UK and San Francisco

Company name
web address www.brightmoorpath.com
email director@brightmoorpath.com
Facebook brightmoor path
LinkedIn Brightmoor Path
Twitter Brightmoor Path
Telephone: +44 (0) 712 348 9561

Logo Text

Something that symbolises unlimited growth - probably not text - could use the word INSIGHT in some way

Number of Pages Required

1 page

Colors
e4daeb
f3f1f8
ffffff

Requirements
Must have
• social media symbols and address
• company name
• Harriet Lomax
• Director
• Telephone +44 (0) 712 348 9561
• Website name www.brightmoorpath.co.uk
• Reverse of Card:
• Discreet, Fast, Brightmoor Consultancy
• Corporate, Professional, Personal & Property Investment
Nice to have
• not too angular; soft lines; not too cluttered (possibly social media on the reverse and just logo, name, number on the front?
Should not have
• too busy

```html
<!DOCTYPE html>
<html lang="en">
<head>
<meta charset="utf-8">
<title>Brightmoor Paths</title>
<link href="https://fonts.googleapis.com/css2?family=Roboto:wght@300;400;500;700&display=swap" rel="stylesheet">
<style>
:root{
  --brand:#372388;
  --brand-dark:#2e1d78;
  --ink:#2f2f33;
  --muted:#8a8a90;
  --line:#dcdce2;
  --hero-bg:#f1f1f3;
  --band-bg:#f3f3f5;
  --white:#ffffff;
}
*{margin:0;padding:0;box-sizing:border-box}
html,body{width:1044px;height:1200px;overflow:hidden}
body{font-family:"Roboto",Arial,sans-serif;color:var(--ink);background:var(--white);position:relative}
.abs{position:absolute}

/* header */
.site-header{position:absolute;left:0;top:0;width:1044px;height:60px;background:var(--white);border-bottom:1px solid #ececf0;z-index:2}
.brand{left:77px;top:17px;display:flex;align-items:center;gap:7px;font-size:20px;font-weight:500;color:var(--ink);letter-spacing:.2px}
.brand-dot{width:12px;height:12px;border-radius:50%;background:var(--brand)}
.nav{left:356px;top:25px;display:flex;gap:0;font-size:10.4px;font-weight:400;color:var(--ink);letter-spacing:.1px}
.nav span{margin-right:25px}
.btn-outline{left:871px;top:14px;width:95px;height:32px;border:1px solid var(--brand);color:var(--brand);font-size:10.4px;display:flex;align-items:center;justify-content:center}

/* hero */
.hero{left:0;top:60px;width:1044px;height:410px;background:var(--hero-bg)}
.hero-photo{left:640px;top:60px;width:404px;height:410px;background:linear-gradient(120deg,#eeeef1 0%,#e4e6ee 45%,#d9dbe4 100%)}
.hero-intro{left:77px;top:166px;font-size:27px;font-weight:300;color:#6f6f74}
.hero-title{left:76px;top:200px;font-size:35px;font-weight:300;color:var(--ink)}
.hero-title em{font-style:normal;color:var(--brand)}
.hero-text{left:77px;top:257px;width:340px;font-size:12px;line-height:17px;color:#3b3b40}
.btn-solid{left:77px;top:312px;width:97px;height:35px;background:var(--brand);color:var(--white);font-size:10.4px;font-weight:500;display:flex;align-items:center;justify-content:center}
.dots{left:77px;top:422px;display:flex;gap:4px}
.dots i{width:8px;height:8px;border-radius:50%;border:1px solid #555;display:block}
.dots i.on{background:var(--brand);border-color:var(--brand)}

/* welcome */
.welcome-photo{left:0;top:470px;width:356px;height:336px;background:linear-gradient(180deg,#8d8690 0%,#5e5a60 45%,#3f3d42 100%)}
.play{left:147px;top:606px;width:64px;height:64px;border-radius:50%;background:rgba(255,255,255,.22)}
.welcome-panel{left:356px;top:470px;width:688px;height:336px;background:var(--brand)}
.welcome-title{left:396px;top:518px;font-size:19px;font-weight:300;color:var(--white)}
.welcome-copy{left:396px;top:555px;width:580px;font-size:11.2px;line-height:17px;color:var(--white)}
.welcome-copy p{margin-bottom:17px}

/* services */
.services-title{left:0;top:840px;width:1044px;text-align:center;font-size:19px;font-weight:300;color:var(--ink)}
.divider{top:892px;width:1px;height:148px;background:var(--line)}
.service{top:892px}
.service svg{display:block;margin-left:0}
.service h3{font-size:16px;font-weight:300;color:#77777c;margin-top:6px;margin-bottom:9px}
.service.dark h3{color:var(--ink)}
.service li{list-style:none;font-size:11.5px;line-height:23.3px;color:#3b3b40}

/* contact band */
.contact-band{left:0;top:1078px;width:1044px;height:84px;background:var(--band-bg)}
.chat-copy{left:77px;top:1099px;font-size:16px;line-height:23px;font-weight:300;color:#3a3a3f}
.contact-item{top:1100px;display:flex;gap:12px}
.contact-item strong{display:block;font-size:15.5px;font-weight:400;color:var(--ink)}
.contact-item small{display:block;font-size:11.2px;color:var(--muted);margin-top:7px}

/* footer */
.site-footer{left:0;top:1162px;width:1044px;height:38px;background:var(--brand);color:var(--white);font-size:10px;display:flex;align-items:center;justify-content:center}
</style>
</head>
<body>

<header class="site-header">
  <div class="abs brand"><span class="brand-dot"></span>Brightmoor Paths</div>
  <nav class="abs nav">
    <span>ABOUT YOU</span><span>ABOUT US</span><span>OUR VALUES</span><span>TESTIMONIALS</span><span>SOCIAL MEDIA</span><span>NEWS ALERT</span>
  </nav>
  <div class="abs btn-outline">CONTACT US</div>
</header>

<section>
  <div class="abs hero"></div>
  <div class="abs hero-photo" role="img" aria-label="Desk with printed charts, a pen, glasses and a smartphone"></div>
  <div class="abs hero-intro">Welcome to</div>
  <h1 class="abs hero-title" style="font-weight:300">Brightmoor <em>Paths</em></h1>
  <p class="abs hero-text">Our main message is helping people move to the next level - through investments, personal and professional growth</p>
  <div class="abs btn-solid">LEARN MORE</div>
  <div class="abs dots"><i class="on"></i><i></i><i></i></div>
</section>

<section>
  <div class="abs welcome-photo" role="img" aria-label="Person on a sofa working on a laptop at a small orange table"></div>
  <div class="abs play">
    <svg width="64" height="64" viewBox="0 0 64 64" fill="none" stroke="#fff" stroke-width="1.3">
      <rect x="21" y="24" width="22" height="16"/>
      <line x1="25" y1="24" x2="25" y2="40"/><line x1="39" y1="24" x2="39" y2="40"/>
      <path d="M30 28.5 L35 32 L30 35.5 Z"/>
    </svg>
  </div>
  <div class="abs welcome-panel"></div>
  <h2 class="abs welcome-title">Hello and welcome</h2>
  <div class="abs welcome-copy">
    <p>to the company that works with you on your terms.</p>
    <p>If you seek an experienced and trusted partner to work with you on an assignment or simply want some strategies to move your personal or professional talents to the next level then you are in the right place.</p>
    <p>If you feel that the pace of change in business is so fast that to be an outstanding leader you should ensure you are brought up to speed regularly then you are in the right place.</p>
    <p>If you are hearing about the essential new leadership essentials and you are ready to hear how to adopt them into your life or business then you are at the right place.</p>
    <p>I am so convinced that you will be delighted with how fast you can make change happen.</p>
  </div>
</section>

<section>
  <h2 class="abs services-title">Services</h2>
  <div class="abs divider" style="left:374px"></div>
  <div class="abs divider" style="left:670px"></div>

  <div class="abs service" style="left:147px">
    <svg width="26" height="24" viewBox="0 0 26 24" fill="none" stroke="#333" stroke-width="1.1">
      <circle cx="8" cy="5" r="4"/><path d="M4 23 V13 a4 4 0 0 1 8 0 V23"/>
      <circle cx="18" cy="16" r="4.5" fill="var(--brand)" stroke="none"/>
    </svg>
    <h3>Consultancy</h3>
    <ul><li>Professional and Personal</li><li>Next Generation Leaders (16-30)</li><li>Consultation Options</li></ul>
  </div>

  <div class="abs service" style="left:452px">
    <svg width="26" height="24" viewBox="0 0 26 24" fill="none" stroke="#333" stroke-width="1.1">
      <rect x="2" y="2" width="21" height="14"/><circle cx="12.5" cy="9" r="4"/>
      <path d="M12.5 5 A4 4 0 0 1 16.5 9 H12.5 Z" fill="var(--brand)" stroke="none"/>
      <path d="M12.5 16 V19 M9 23 L12.5 19 L16 23"/>
    </svg>
    <h3>On Assignment</h3>
    <ul><li>Team Cohesion Strategy</li><li>Go To Market Strategy</li><li>Internationalisation Strategy</li></ul>
  </div>

  <div class="abs service dark" style="left:722px">
    <svg width="26" height="24" viewBox="0 0 26 24" fill="none" stroke="#333" stroke-width="1.1">
      <circle cx="12" cy="6" r="4.5"/><path d="M2 23 C2 16 7 13 12 13 C17 13 22 16 22 23 Z"/>
      <path d="M9 18 L11.5 20.5 L16 16" stroke="var(--brand)" stroke-width="1.4"/>
    </svg>
    <h3>Property: Private Client</h3>
    <ul><li>Promotion and cash-buyer matching</li><li>Investment: high return projects</li><li>Commercial: Hotels and Senior Housing</li><li>Prestige Residential: US, Australia, UK</li></ul>
  </div>
</section>

<section>
  <div class="abs contact-band"></div>
  <p class="abs chat-copy">Let’s chat, if you want a non committal<br>conversation get in touch by email or telephone.</p>
  <div class="abs contact-item" style="left:596px">
    <svg width="38" height="38" viewBox="0 0 38 38" fill="none" stroke="var(--brand)" stroke-width="1.5" style="margin-top:2px">
      <path d="M8 4 L14 10 L10 15 C12 21 17 26 23 28 L28 24 L34 30 L29 35 C16 33 5 22 3 9 Z"/>
      <path d="M22 6 A10 10 0 0 1 32 16 M22 11 A5 5 0 0 1 27 16"/>
    </svg>
    <div><strong>( 415 ) 630 - 2184</strong><small>Get in Touch, Call Us</small></div>
  </div>
  <div class="abs contact-item" style="left:807px">
    <svg width="48" height="38" viewBox="0 0 48 38" fill="none" stroke="var(--brand)" stroke-width="1.5" style="margin-top:2px">
      <rect x="1" y="3" width="46" height="33"/><path d="M1 3 L24 22 L47 3 M1 36 L18 17 M47 36 L30 17"/>
    </svg>
    <div><strong>info@bmpaths.com</strong><small>Email us</small></div>
  </div>
</section>

<footer class="abs site-footer">Brightmoor Path Limited, registered in England and Wales. Registeres number 10482915</footer>

</body>
</html>
```